Need design for an App.

The app in question is related to security and crime events with real time feed, engagement with friends and posting pictures, we want a sleak, minimal style. There are 11 or 12 screens to be made. We are adding video file as suggestion. We are not sure about colors so we accept suggestions. We are also adding the logo.

Reason: Just giving more time to designers. Thanks.

Industry/Entity Type

Security

Font styles to use
Sans Serif

Requirements
Must have
• The app must have a Login view; a new user view (with nickname, email and pass); a retrieve pass view; a menu view with options for alert configuration, send emergency alert and send report, a feed view with the most popular reports (3 worldwide at the top and near reports after), a profile view with avatar and personal reports, a send emergency alert view with a camera view; a configuration view when the user can put up to 5 contacts to send the alert to them;a send report view with camera and options to configure the camera; a edit report view where the user can see the 3 photos he will update and add a comment of those photos.
Nice to have
• Check the files we are open minds
Should not have
• old design

```html
<!DOCTYPE html>
<html lang="en">
<head>
<meta charset="utf-8">
<title>Vigila – Onboarding Screens</title>
<link href="https://fonts.googleapis.com/css2?family=Roboto:wght@400;500;700&display=swap" rel="stylesheet">
<style>
  :root {
    --brand-red: #c51d3b;
    --brand-red-deep: #b2182f;
    --ink: #1f1f1f;
    --button-dark: #262626;
    --field: #e4e4e4;
    --field-prefix: #d6d6d6;
    --placeholder: #b4b4b4;
    --page: #f4f5f7;
    --white: #ffffff;
    --frame: #111111;
    --avatar-tone: #8a6f5e;
  }
  * { box-sizing: border-box; margin: 0; padding: 0; }
  html, body { width: 1200px; height: 675px; overflow: hidden; }
  body {
    background: var(--page);
    font-family: "Roboto", Arial, sans-serif;
    color: var(--ink);
    position: relative;
  }
  .screen {
    position: absolute;
    top: 124px;
    width: 240px;
    height: 426px;
    background: var(--white);
    border: 2px solid var(--frame);
    overflow: hidden;
    box-shadow: 0 10px 30px rgba(0,0,0,0.08);
  }
  .screen--splash { left: 82px; background: var(--brand-red); }
  .screen--login { left: 493px; }
  .screen--contacts { left: 866px; }

  /* status bar */
  .status-bar {
    position: absolute; top: 0; left: 0; right: 0; height: 18px;
    display: flex; align-items: center; justify-content: space-between;
    padding: 0 6px; font-size: 8.5px; color: var(--ink);
  }
  .screen--splash .status-bar { color: var(--white); background: var(--brand-red-deep); }
  .status-bar__left, .status-bar__right { display: flex; align-items: center; gap: 3px; width: 70px; }
  .status-bar__right { justify-content: flex-end; }
  .status-bar__time { font-weight: 500; }
  .status-bar svg { display: block; }

  /* splash */
  .splash__backdrop {
    position: absolute; inset: 18px 0 0 0;
    background: linear-gradient(180deg, #c9314a 0%, #c21f3b 50%, #b8203a 100%);
  }
  .splash__brand {
    position: absolute; left: 0; right: 0; top: 132px;
    display: flex; flex-direction: column; align-items: center; gap: 14px;
  }
  .splash__dot { width: 84px; height: 84px; border-radius: 50%; background: var(--white); }
  .splash__name { color: var(--white); font-size: 30px; font-weight: 500; letter-spacing: 0.5px; }
  .splash__company {
    position: absolute; bottom: 16px; left: 0; right: 0;
    text-align: center; color: var(--white); font-size: 8px;
  }

  /* login */
  .login__name {
    position: absolute; top: 38px; left: 0; right: 0;
    text-align: center; color: var(--brand-red); font-size: 28px; font-weight: 500;
  }
  .login__welcome {
    position: absolute; top: 104px; left: 0; right: 0; text-align: center;
    font-size: 10.5px; font-weight: 500;
  }
  .login__title {
    position: absolute; top: 118px; left: 0; right: 0; text-align: center;
    font-size: 13.5px; font-weight: 500;
  }
  .field {
    position: absolute; left: 25px; width: 189px; height: 31px;
    background: var(--field); font-size: 9.5px; color: var(--placeholder);
    padding-left: 7px; display: flex; align-items: center;
  }
  .field--username { top: 158px; }
  .field--password { top: 196px; letter-spacing: 1px; }
  .button {
    position: absolute; left: 37px; width: 166px; height: 31px;
    display: flex; align-items: center; justify-content: center;
    font-size: 10px; color: var(--white); font-weight: 400;
  }
  .button--login { top: 239px; background: var(--button-dark); }
  .button--new-user { top: 278px; background: var(--brand-red); }
  .button--finish { top: 374px; background: var(--brand-red); }
  .login__help {
    position: absolute; bottom: 16px; left: 0; right: 0; text-align: center;
    font-size: 8.5px; font-weight: 500;
  }

  /* contacts */
  .avatar {
    position: absolute; top: 29px; left: 89px; width: 61px; height: 61px;
    border-radius: 50%; border: 2px solid var(--brand-red);
    box-shadow: inset 0 0 0 2px var(--white);
    background: var(--avatar-tone);
  }
  .contact { position: absolute; left: 23px; width: 189px; }
  .contact__label {
    display: flex; justify-content: space-between;
    font-size: 9px; font-weight: 500; padding: 0 2px 0 1px; height: 13px;
  }
  .contact__index { color: var(--brand-red); font-weight: 700; }
  .contact__field { display: flex; height: 31px; background: var(--field); }
  .contact__prefix {
    width: 35px; background: var(--field-prefix); font-size: 9.5px;
    display: flex; align-items: center; padding-left: 8px;
  }
</style>
</head>
<body>

<!-- Splash -->
<section class="screen screen--splash">
  <div class="splash__backdrop" role="img" aria-label="Collage of smiling people tinted in brand red"></div>
  <div class="status-bar">
    <div class="status-bar__left">
      <svg width="22" height="5" viewBox="0 0 22 5"><g fill="currentColor"><circle cx="2" cy="2.5" r="2"/><circle cx="6.5" cy="2.5" r="2"/><circle cx="11" cy="2.5" r="2"/></g><g fill="none" stroke="currentColor" stroke-width="0.7"><circle cx="15.5" cy="2.5" r="1.7"/><circle cx="20" cy="2.5" r="1.7"/></g></svg>
      <span>CELL</span>
      <svg width="9" height="7" viewBox="0 0 9 7"><path d="M0.5 2.5a6 6 0 0 1 8 0M2 4a3.8 3.8 0 0 1 5 0" fill="none" stroke="currentColor" stroke-width="0.9"/><circle cx="4.5" cy="6" r="0.9" fill="currentColor"/></svg>
    </div>
    <span class="status-bar__time">4:21 PM</span>
    <div class="status-bar__right">
      <svg width="5" height="8" viewBox="0 0 5 8"><path d="M0.5 2l4 3.5L2.5 7V1l2 1.5-4 3.5" fill="none" stroke="currentColor" stroke-width="0.7"/></svg>
      <span>22%</span>
      <svg width="18" height="7" viewBox="0 0 18 7"><rect x="0.4" y="0.4" width="15.5" height="6.2" rx="1" fill="none" stroke="currentColor" stroke-width="0.8"/><rect x="1.5" y="1.5" width="3.5" height="4" fill="currentColor"/><rect x="16.3" y="2.3" width="1.2" height="2.4" fill="currentColor"/></svg>
    </div>
  </div>
  <div class="splash__brand">
    <div class="splash__dot"></div>
    <div class="splash__name">vigila</div>
  </div>
  <div class="splash__company">Company Name</div>
</section>

<!-- Login -->
<section class="screen screen--login">
  <div class="status-bar">
    <div class="status-bar__left">
      <svg width="22" height="5" viewBox="0 0 22 5"><g fill="currentColor"><circle cx="2" cy="2.5" r="2"/><circle cx="6.5" cy="2.5" r="2"/><circle cx="11" cy="2.5" r="2"/></g><g fill="none" stroke="currentColor" stroke-width="0.7"><circle cx="15.5" cy="2.5" r="1.7"/><circle cx="20" cy="2.5" r="1.7"/></g></svg>
      <span>CELL</span>
      <svg width="9" height="7" viewBox="0 0 9 7"><path d="M0.5 2.5a6 6 0 0 1 8 0M2 4a3.8 3.8 0 0 1 5 0" fill="none" stroke="currentColor" stroke-width="0.9"/><circle cx="4.5" cy="6" r="0.9" fill="currentColor"/></svg>
    </div>
    <span class="status-bar__time">4:21 PM</span>
    <div class="status-bar__right">
      <svg width="5" height="8" viewBox="0 0 5 8"><path d="M0.5 2l4 3.5L2.5 7V1l2 1.5-4 3.5" fill="none" stroke="currentColor" stroke-width="0.7"/></svg>
      <span>22%</span>
      <svg width="18" height="7" viewBox="0 0 18 7"><rect x="0.4" y="0.4" width="15.5" height="6.2" rx="1" fill="none" stroke="currentColor" stroke-width="0.8"/><rect x="1.5" y="1.5" width="3.5" height="4" fill="currentColor"/><rect x="16.3" y="2.3" width="1.2" height="2.4" fill="currentColor"/></svg>
    </div>
  </div>
  <div class="login__name">vigila</div>
  <p class="login__welcome">Welcome to Vigila</p>
  <h1 class="login__title">Sign Up Here</h1>
  <div class="field field--username">username</div>
  <div class="field field--password">••••••••</div>
  <div class="button button--login">Login</div>
  <div class="button button--new-user">New User</div>
  <p class="login__help">Need help?</p>
</section>

<!-- Emergency contacts -->
<section class="screen screen--contacts">
  <div class="status-bar">
    <div class="status-bar__left">
      <svg width="22" height="5" viewBox="0 0 22 5"><g fill="currentColor"><circle cx="2" cy="2.5" r="2"/><circle cx="6.5" cy="2.5" r="2"/><circle cx="11" cy="2.5" r="2"/></g><g fill="none" stroke="currentColor" stroke-width="0.7"><circle cx="15.5" cy="2.5" r="1.7"/><circle cx="20" cy="2.5" r="1.7"/></g></svg>
      <span>CELL</span>
      <svg width="9" height="7" viewBox="0 0 9 7"><path d="M0.5 2.5a6 6 0 0 1 8 0M2 4a3.8 3.8 0 0 1 5 0" fill="none" stroke="currentColor" stroke-width="0.9"/><circle cx="4.5" cy="6" r="0.9" fill="currentColor"/></svg>
    </div>
    <span class="status-bar__time">4:21 PM</span>
    <div class="status-bar__right">
      <svg width="5" height="8" viewBox="0 0 5 8"><path d="M0.5 2l4 3.5L2.5 7V1l2 1.5-4 3.5" fill="none" stroke="currentColor" stroke-width="0.7"/></svg>
      <span>22%</span>
      <svg width="18" height="7" viewBox="0 0 18 7"><rect x="0.4" y="0.4" width="15.5" height="6.2" rx="1" fill="none" stroke="currentColor" stroke-width="0.8"/><rect x="1.5" y="1.5" width="3.5" height="4" fill="currentColor"/><rect x="16.3" y="2.3" width="1.2" height="2.4" fill="currentColor"/></svg>
    </div>
  </div>
  <div class="avatar" role="img" aria-label="User profile photo"></div>

  <div class="contact" style="top:100px">
    <div class="contact__label"><span>Emergency Contact No</span><span class="contact__index">01</span></div>
    <div class="contact__field"><span class="contact__prefix">+1</span></div>
  </div>
  <div class="contact" style="top:151px">
    <div class="contact__label"><span>Emergency Contact No</span><span class="contact__index">02</span></div>
    <div class="contact__field"><span class="contact__prefix">+1</span></div>
  </div>
  <div class="contact" style="top:202px">
    <div class="contact__label"><span>Emergency Contact No</span><span class="contact__index">03</span></div>
    <div class="contact__field"><span class="contact__prefix">+1</span></div>
  </div>
  <div class="contact" style="top:257px">
    <div class="contact__label"><span>Emergency Contact No</span><span class="contact__index">04</span></div>
    <div class="contact__field"><span class="contact__prefix">+1</span></div>
  </div>
  <div class="contact" style="top:310px">
    <div class="contact__label"><span>Emergency Contact No</span><span class="contact__index">05</span></div>
    <div class="contact__field"><span class="contact__prefix">+1</span></div>
  </div>

  <div class="button button--finish">Finish</div>
</section>

</body>
</html>
```